Aunt's Find Calm - Graphic Pic for Book Cover

I need a BOOK Cover design that has Logo incorporated:
Aunt's Find Calm
Book Size 5x7.

This is a play on the word HIGH - which really is just a feeling people may get when they are out in nature. NOT cartoon looking.

Book Cover Words:
Aunt’s Find Calm: That Edge of the Meadow Glow
PS. No Drugs or Alcohol Needed.

I am writing an inspirational book called Aunt’s Find Calm. It is about hard working, determined mothers with dreams of living the good life while raising successful children along the way. The only problem is that most Mother’s have so many responsibilities that they put upon themselves that sometimes they get stuck in a routine and become fearful of adventure and taking risks. As a result, women lose their sense of freedom and do not take much-needed alone time. Yet, ultimately Mother’s can learn to take a break, which can solve many problems and propel them on to a new trail that may include the high country!
Updates

HI.I am looking forward to your designs!! Added Friday, May 1, 2015

Target Market(s)

Mothers of all ages, from 18 to 80

Logo Text

Aunt's Find Calm

Logo styles of interest
Pictorial/Combination Logo
Colors
f68e4e
f68d4d
faa54b
ffc214
fbed22
f04a50

Requirements
Must have
• Colorful, like sunset colors. Vibrant, Fun...
• Words on it:
• Aunt's Find Calm.
• Edge of the Meadow Glow.
• P.S. No Drugs or Alcohol Needed
Nice to have
• I like the billboard idea with logo in it.
• Road into mountain
• Words on it: Aunt's Find Calm. Edge of the Meadow Glow.
• The book cover, website logo all need to tie together.
Should not have
• Attached are some rough ideas...that I drew up. and a image that might be able to be used.

```html
<!DOCTYPE html>
<html lang="en">
<head>
<meta charset="utf-8">
<title>Aunt's Find Calm — Book Cover</title>
<link rel="stylesheet" href="https://fonts.googleapis.com/css2?family=Playfair+Display:wght@900&family=Orbitron:wght@500&family=Archivo+Black&display=swap">
<style>
  :root {
    --sunset-red: #e8353c;
    --sunset-coral: #f04a50;
    --sunset-orange: #f68d4d;
    --sunset-amber: #faa54b;
    --title-cream: #fbe7c6;
    --note-peach: #f6a46a;
    --note-shadow: rgba(120, 60, 30, 0.55);
    --tagline-yellow: #fbed22;
    --sky-pale: #dfe9ee;
    --sky-haze: #b9ccd6;
    --hill-green: #5f6f4a;
    --rock-brown: #8a6d4e;
  }
  * { margin: 0; padding: 0; box-sizing: border-box; }
  html, body {
    width: 857px;
    height: 1200px;
    overflow: hidden;
    background: #ffffff;
  }
  .cover {
    position: relative;
    width: 857px;
    height: 1200px;
    overflow: hidden;
    background:
      radial-gradient(ellipse 60% 40% at 85% 20%, var(--sunset-amber) 0%, transparent 70%),
      radial-gradient(ellipse 55% 35% at 20% 85%, var(--sunset-amber) 0%, transparent 70%),
      linear-gradient(180deg, var(--sunset-coral) 0%, var(--sunset-orange) 45%, var(--sunset-red) 100%);
  }
  .masthead {
    position: absolute;
    left: 0; top: 0;
    width: 100%;
    height: 345px;
    background:
      radial-gradient(ellipse 45% 60% at 80% 35%, rgba(250,165,75,0.9) 0%, transparent 70%),
      radial-gradient(ellipse 40% 50% at 10% 15%, rgba(232,53,60,0.9) 0%, transparent 70%),
      linear-gradient(160deg, var(--sunset-red) 0%, var(--sunset-orange) 60%, var(--sunset-amber) 100%);
  }
  .brand {
    position: absolute;
    left: 48px;
    top: 118px;
    display: flex;
    align-items: center;
    gap: 16px;
  }
  .brand-mark {
    width: 64px;
    height: 64px;
    border-radius: 50%;
    background: var(--sunset-amber);
    flex: none;
  }
  .brand-name {
    font-family: "Playfair Display", Georgia, serif;
    font-weight: 900;
    font-size: 68px;
    letter-spacing: 2px;
    text-transform: uppercase;
    color: var(--title-cream);
    line-height: 1;
    white-space: nowrap;
  }
  .hero {
    position: absolute;
    left: 0;
    top: 345px;
    width: 100%;
    height: 578px;
  }
  .hero-scene {
    position: absolute;
    inset: 0;
    background:
      radial-gradient(ellipse 35% 25% at 12% 12%, #ffffff 0%, transparent 70%),
      linear-gradient(180deg, var(--sky-pale) 0%, var(--sky-haze) 38%, #8d9a8c 52%, var(--hill-green) 68%, var(--rock-brown) 86%, #6d5239 100%);
  }
  .hero-note {
    position: absolute;
    left: 524px;
    top: 48px;
    width: 310px;
    font-family: "Orbitron", "Courier New", monospace;
    font-weight: 500;
    font-size: 34px;
    line-height: 1.2;
    color: var(--note-peach);
    text-shadow: 1px 1px 2px var(--note-shadow);
  }
  .hero-tagline {
    position: absolute;
    left: 28px;
    top: 490px;
    font-family: "Archivo Black", Arial, sans-serif;
    font-size: 41px;
    letter-spacing: 0.5px;
    text-transform: uppercase;
    color: var(--tagline-yellow);
    text-shadow: 2px 2px 3px rgba(40,30,10,0.7);
    white-space: nowrap;
  }
  .footer-band {
    position: absolute;
    left: 0;
    top: 923px;
    width: 100%;
    height: 277px;
    background:
      radial-gradient(ellipse 50% 45% at 25% 60%, rgba(250,165,75,0.85) 0%, transparent 70%),
      radial-gradient(ellipse 40% 45% at 85% 40%, rgba(232,53,60,0.85) 0%, transparent 70%),
      linear-gradient(180deg, var(--sunset-red) 0%, var(--sunset-orange) 55%, var(--sunset-coral) 100%);
  }
</style>
</head>
<body>
  <main class="cover">
    <header class="masthead">
      <div class="brand">
        <span class="brand-mark" aria-hidden="true"></span>
        <h1 class="brand-name">Aunt’s Find Calm</h1>
      </div>
    </header>

    <section class="hero">
      <div class="hero-scene" role="img" aria-label="Photograph of a woman standing on a rocky mountain summit with arms spread wide, a backpack at her feet, overlooking hazy forested valleys under a bright sky"></div>
      <p class="hero-note">No Drugs or Alcohol Needed</p>
      <p class="hero-tagline">Edge of the Meadow Glow</p>
    </section>

    <footer class="footer-band" aria-hidden="true"></footer>
  </main>
</body>
</html>
```